Website for Industrial Maintenance Consulting Firm
BOLTSTEADY
Website for Industrial Maintenance Consulting Firm - Consulting
Creative Brief
Consulting
www.boltsteady-example.com (currently a blank page)
We provide consulting services to manufacturing firms to help them improve the reliability of their plant equipment and maintenance processes.
Likes: Clean, Simple, Easy Navigation, Cohesive color schemes Dislikes: Cliche pictures
Nav menu should include: Home, Services, About, Contact
BrightPixelCrafter BrightPixelCrafter
Hi CO, Please check your private message. thanks, BrightPixelCrafter
grovelark grovelark
Designers, Here are picturevault item #'s to some images that we like. 41865203 (our favorite) 572913608 318470562-004 26390415 59023741 FAB_417 63148097
QUIKLAYOUTS QUIKLAYOUTS
Dear sir, Please check your private messege Thanks.
Designers, Please use images that depict manufacturing processes or industrial maintenance activities. Thanks. Milo
PortalKeeper PortalKeeper
Designers, Please only use images provided by the project holder. If in case source of images has not been provided, you are requested to use images from “www.picturevaultimages-example.com”. Images used from any other website or source will not be accepted. In case you are using images from “www.picturevaultimages-example.com”, please make sure to keep a record of image ID numbers as contest winners will be required to provide those ID's. Regards, QT/RVN/HK Team
Dynamic Nav Menu Home Services -Full Plant Checkup -Uptime Groundwork -Steady Care Method -All Services About Contact
Would also like a contact form on the contact page. Fields should include: First Name: Last Name: Title: Company: City: State: Phone: Email:

```html
<!DOCTYPE html>
<html lang="en">
<head>
<meta charset="utf-8">
<title>BOLTSTEADY – Maintenance &amp; Reliability Processes</title>
<link rel="stylesheet" href="https://fonts.googleapis.com/css2?family=Arimo:wght@400;700&family=Roboto+Condensed:wght@700&display=swap">
<style>
  :root {
    --black: #000000;
    --brand-blue: #1e5fad;
    --brand-blue-light: #6e8fd2;
    --link-blue: #2a6ab8;
    --nav-blue-top: #4d8ad6;
    --nav-blue-bottom: #1f5ca8;
    --nav-grey-top: #777777;
    --nav-grey-bottom: #3a3a3a;
    --panel: #f5f5f5;
    --rule: #d8d8d8;
    --text-dark: #111111;
    --text-grey: #555555;
    --footer: #262626;
    --footer-text: #a9a9a9;
    --white: #ffffff;
  }
  * { box-sizing: border-box; margin: 0; padding: 0; }
  html, body { width: 1200px; height: 878px; overflow: hidden; background: var(--black); }
  body { position: relative; font-family: "Arimo", Arial, sans-serif; }

  .site-header { position: absolute; left: 0; top: 0; width: 1200px; height: 133px; }
  .brand { position: absolute; left: 162px; top: 38px; display: flex; align-items: center; gap: 10px; }
  .brand-dot { width: 56px; height: 56px; border-radius: 50%; background: var(--brand-blue); }
  .brand-text { display: flex; flex-direction: column; }
  .brand-name { font-weight: 700; font-size: 32px; color: var(--link-blue); letter-spacing: 0.5px; line-height: 1; }
  .brand-tag { font-size: 12px; color: #8a8a8a; margin-top: 4px; }

  .call { position: absolute; left: 818px; top: 66px; display: flex; align-items: center; gap: 6px; font-size: 21px; }
  .call-label { color: var(--white); font-weight: 700; }
  .call-number { color: var(--link-blue); }

  .main-nav { position: absolute; left: 481px; top: 99px; width: 587px; height: 34px; display: flex; }
  .main-nav a {
    display: flex; align-items: center; justify-content: center;
    color: var(--white); text-decoration: none; font-size: 14px; font-weight: 700;
    background: linear-gradient(var(--nav-blue-top), var(--nav-blue-bottom));
    border-right: 1px solid #0f3f7c;
  }
  .main-nav a.is-current { background: linear-gradient(var(--nav-grey-top), var(--nav-grey-bottom)); }
  .main-nav a:last-child { border-right: none; border-top-right-radius: 4px; }
  .main-nav a:first-child { border-top-left-radius: 4px; }

  .hero { position: absolute; left: 0; top: 133px; width: 1200px; height: 366px; background: var(--brand-blue); }
  .hero-art { position: absolute; left: 0; top: 0; }
  .hero-copy { position: absolute; left: 170px; top: 30px; color: var(--white); }
  .hero-title { font-family: "Roboto Condensed", "Arial Narrow", sans-serif; line-height: 1; }
  .hero-title .l1 { font-size: 38px; display: block; }
  .hero-title .l1 b { font-family: "Arimo", Arial, sans-serif; font-size: 42px; letter-spacing: 2px; }
  .hero-title .l2 { font-family: "Arimo", Arial, sans-serif; font-size: 46px; letter-spacing: 4px; display: block; margin-top: -2px; }
  .hero-title .l3 { font-size: 34px; letter-spacing: 11px; display: block; margin-top: -2px; }
  .hero-list { list-style: none; margin-top: 24px; }
  .hero-list li { display: flex; align-items: center; gap: 8px; font-size: 17.5px; height: 28px; }
  .read-more {
    position: absolute; left: 173px; top: 301px; width: 207px; height: 36px; border-radius: 18px;
    background: linear-gradient(#4a4a4a, #0d0d0d); color: var(--white); font-weight: 700; font-size: 16px;
    display: flex; align-items: center; justify-content: center; text-decoration: none;
    box-shadow: 0 10px 8px -6px rgba(255,255,255,0.25);
  }

  .programs {
    position: absolute; left: 169px; top: 527px; width: 896px; height: 257px;
    background: var(--panel); border-radius: 8px; display: flex; padding: 13px 0;
  }
  .program { position: relative; padding-left: 60px; border-right: 2px solid var(--rule); }
  .program:last-child { border-right: none; }
  .program:nth-child(1) { flex: 0 0 298px; }
  .program:nth-child(2) { flex: 0 0 304px; }
  .program:nth-child(3) { flex: 1; }
  .program h2 { font-size: 20px; color: var(--text-dark); margin-top: 22px; font-weight: 700; white-space: nowrap; }
  .program-name {
    height: 70px; display: flex; align-items: center;
    font-size: 21px; font-weight: 700; color: var(--brand-blue); white-space: nowrap;
  }
  .program ul { list-style: none; margin-top: 8px; margin-left: 2px; }
  .program li { display: flex; align-items: center; gap: 5px; font-size: 13.5px; color: var(--text-grey); height: 18px; white-space: nowrap; }
  .learn-more { position: absolute; left: 166px; top: 221px; font-size: 14px; color: var(--text-dark); text-decoration: none; }

  .site-footer {
    position: absolute; left: 0; top: 812px; width: 1200px; height: 47px; background: var(--footer);
    color: var(--footer-text); font-size: 13.5px; display: flex; align-items: center; justify-content: center; gap: 6px;
  }
  .site-footer b { font-weight: 700; margin: 0 4px; }
</style>
</head>
<body>
  <header class="site-header">
    <div class="brand">
      <span class="brand-dot"></span>
      <div class="brand-text">
        <span class="brand-name">BOLTSTEADY</span>
        <span class="brand-tag">Maintenance &amp; Reliability Processes</span>
      </div>
    </div>
    <div class="call">
      <svg width="18" height="24" viewBox="0 0 18 24" aria-hidden="true"><path d="M4 1 L8 6 L6 9 Q7 14 11 17 L14 15 L17 19 L14 23 Q2 18 1 4 Z" fill="#2a6ab8"/></svg>
      <span class="call-label">Call:</span>
      <span class="call-number">(555) 014-2270</span>
    </div>
    <nav class="main-nav">
      <a href="#" class="is-current" style="width:113px">HOME</a>
      <a href="#" style="width:156px">ABOUT US</a>
      <a href="#" style="width:152px">SERVICES</a>
      <a href="#" style="width:166px">CONTACT US</a>
    </nav>
  </header>

  <section class="hero">
    <svg class="hero-art" width="1200" height="366" viewBox="0 0 1200 366">
      <defs>
        <linearGradient id="panelGlow" x1="0" x2="1" y1="0" y2="0">
          <stop offset="0" stop-color="#1e5fad"/>
          <stop offset="1" stop-color="#7190d2"/>
        </linearGradient>
        <linearGradient id="plantTones" x1="0" x2="1" y1="0" y2="1">
          <stop offset="0" stop-color="#c9ccd0"/>
          <stop offset="0.5" stop-color="#9aa1a8"/>
          <stop offset="1" stop-color="#b7bcc2"/>
        </linearGradient>
      </defs>
      <polygon points="160,0 500,0 561,181 500,366 160,366" fill="url(#panelGlow)"/>
      <polygon points="481,0 500,0 561,181 500,366 481,366 542,181" fill="#1a4f94"/>
      <polygon points="500,0 520,0 581,181 520,366 500,366 561,181" fill="#5a5a5a"/>
      <polygon role="img" aria-label="Photo: two plant workers in hard hats and safety vests shaking hands in front of refinery equipment" points="520,0 1068,0 1068,366 520,366 581,181" fill="url(#plantTones)"/>
    </svg>
    <div class="hero-copy">
      <h1 class="hero-title">
        <span class="l1">Create a <b>MORE</b></span>
        <span class="l2">RELIABLE</span>
        <span class="l3">Tomorrow</span>
      </h1>
      <ul class="hero-list">
        <li><svg width="20" height="16" viewBox="0 0 20 16" aria-hidden="true"><path d="M1 9 L7 15 L19 1 L7 10 Z" fill="#fff"/></svg>Auditing &amp; Consulting</li>
        <li><svg width="20" height="16" viewBox="0 0 20 16" aria-hidden="true"><path d="M1 9 L7 15 L19 1 L7 10 Z" fill="#fff"/></svg>Equipment Maintenance Plans</li>
        <li><svg width="20" height="16" viewBox="0 0 20 16" aria-hidden="true"><path d="M1 9 L7 15 L19 1 L7 10 Z" fill="#fff"/></svg>Work Order Planning &amp; Scheduling</li>
        <li><svg width="20" height="16" viewBox="0 0 20 16" aria-hidden="true"><path d="M1 9 L7 15 L19 1 L7 10 Z" fill="#fff"/></svg>Customized Services</li>
      </ul>
    </div>
    <a class="read-more" href="#">CLICK TO READ MORE</a>
  </section>

  <section class="programs">
    <article class="program">
      <h2>Assess &amp; Plan</h2>
      <div class="program-name">Full Plant Checkup</div>
      <ul>
        <li><svg width="13" height="11" viewBox="0 0 13 11" aria-hidden="true"><path d="M1 6 L5 10 L12 1 L5 7 Z" fill="#555"/></svg>Full Plant Checkup</li>
        <li><svg width="13" height="11" viewBox="0 0 13 11" aria-hidden="true"><path d="M1 6 L5 10 L12 1 L5 7 Z" fill="#555"/></svg>Uptime Groundwork</li>
        <li><svg width="13" height="11" viewBox="0 0 13 11" aria-hidden="true"><path d="M1 6 L5 10 L12 1 L5 7 Z" fill="#555"/></svg>Steady Care Method</li>
        <li><svg width="13" height="11" viewBox="0 0 13 11" aria-hidden="true"><path d="M1 6 L5 10 L12 1 L5 7 Z" fill="#555"/></svg>All Services</li>
      </ul>
      <a class="learn-more" href="#">Learn more »</a>
    </article>
    <article class="program">
      <h2>Build Your Foundation</h2>
      <div class="program-name">Uptime Groundwork</div>
      <ul>
        <li><svg width="13" height="11" viewBox="0 0 13 11" aria-hidden="true"><path d="M1 6 L5 10 L12 1 L5 7 Z" fill="#555"/></svg>Full Plant Checkup</li>
        <li><svg width="13" height="11" viewBox="0 0 13 11" aria-hidden="true"><path d="M1 6 L5 10 L12 1 L5 7 Z" fill="#555"/></svg>Uptime Groundwork</li>
        <li><svg width="13" height="11" viewBox="0 0 13 11" aria-hidden="true"><path d="M1 6 L5 10 L12 1 L5 7 Z" fill="#555"/></svg>Steady Care Method</li>
        <li><svg width="13" height="11" viewBox="0 0 13 11" aria-hidden="true"><path d="M1 6 L5 10 L12 1 L5 7 Z" fill="#555"/></svg>All Services</li>
      </ul>
      <a class="learn-more" href="#">Learn more »</a>
    </article>
    <article class="program">
      <h2>Execute</h2>
      <div class="program-name">Steady Care Method</div>
      <ul>
        <li><svg width="13" height="11" viewBox="0 0 13 11" aria-hidden="true"><path d="M1 6 L5 10 L12 1 L5 7 Z" fill="#555"/></svg>Full Plant Checkup</li>
        <li><svg width="13" height="11" viewBox="0 0 13 11" aria-hidden="true"><path d="M1 6 L5 10 L12 1 L5 7 Z" fill="#555"/></svg>Uptime Groundwork</li>
        <li><svg width="13" height="11" viewBox="0 0 13 11" aria-hidden="true"><path d="M1 6 L5 10 L12 1 L5 7 Z" fill="#555"/></svg>Steady Care Method</li>
        <li><svg width="13" height="11" viewBox="0 0 13 11" aria-hidden="true"><path d="M1 6 L5 10 L12 1 L5 7 Z" fill="#555"/></svg>All Services</li>
      </ul>
      <a class="learn-more" href="#">Learn more »</a>
    </article>
  </section>

  <footer class="site-footer">
    © Copyright 2012 <b>BOLTSTEADY LLC.</b> All right reserved
  </footer>
</body>
</html>
```